Bref créative
business cards & stationary
Corvell Insulation
Modern
BO KERRIGAN
SALESMAN
14 PELLMORE CT.
BRENTFIELD, CA 95418
bo.kerrigan@corvellinsulation.com
www.corvellinsulation.com
I'd like the edges to be rounded instead of pointed. I would also like little symbols next to the phone, E-mail, website, and fax. For example, near the phone number, a small telephone. Also, if possible, I would like a QR Barcode that leads to my website on the back.

```html
<!DOCTYPE html>
<html lang="en">
<head>
<meta charset="utf-8">
<title>Corvell Insulation – Business Card</title>
<link href="https://fonts.googleapis.com/css2?family=Exo+2:wght@400;600;700&display=swap" rel="stylesheet">
<style>
  :root {
    --page-bg: #e4e4e2;
    --card-white: #ffffff;
    --band-dark: #2f3230;
    --green-light: #a6d63a;
    --green-mid: #6fb52c;
    --green-deep: #3f8a22;
    --text-dark: #2c312b;
    --text-pale: #e8f5c8;
    --brand-green: #6fb52c;
  }
  * { box-sizing: border-box; margin: 0; padding: 0; }
  html, body {
    width: 1200px; height: 902px; overflow: hidden;
    background: var(--page-bg);
    font-family: "Exo 2", sans-serif;
  }
  .canvas { position: relative; width: 1200px; height: 902px; }
  .business-card {
    position: absolute; left: 100px; top: 161px;
    width: 1000px; height: 580px;
    border-radius: 28px; overflow: hidden;
    background: var(--card-white);
    box-shadow: 0 10px 30px rgba(0,0,0,0.18);
  }
  .card-top {
    position: absolute; left: 0; top: 0; width: 100%; height: 222px;
    background: var(--card-white);
  }
  .brand {
    position: absolute; top: 92px; left: 0; width: 100%;
    display: flex; justify-content: center; align-items: center; gap: 18px;
  }
  .brand-square { width: 40px; height: 40px; background: var(--brand-green); border-radius: 4px; }
  .brand-name {
    font-weight: 700; font-size: 40px; letter-spacing: 3px;
    color: var(--text-dark); text-transform: uppercase;
  }
  .card-green {
    position: absolute; left: 0; top: 232px; width: 100%; height: 348px;
    background: radial-gradient(ellipse at 50% 35%, var(--green-light) 0%, var(--green-mid) 55%, var(--green-deep) 100%);
  }
  .divider-band { position: absolute; left: 0; top: 222px; width: 1000px; height: 24px; }
  .person {
    position: absolute; left: 70px; top: 300px;
    color: var(--text-pale); text-transform: uppercase;
  }
  .person-name { font-size: 26px; font-weight: 600; letter-spacing: 2px; }
  .person-role { font-size: 20px; font-weight: 400; letter-spacing: 3px; margin-top: 6px; }
  .contact-list { position: absolute; left: 548px; top: 250px; list-style: none; }
  .contact-item {
    display: flex; align-items: center; gap: 12px;
    height: 30px; font-size: 17px; letter-spacing: 1px;
    color: var(--text-dark); text-transform: uppercase; white-space: nowrap;
  }
  .contact-item.no-icon { padding-left: 34px; }
  .contact-icon { width: 22px; height: 22px; flex: none; }
</style>
</head>
<body>
<main class="canvas">
  <section class="business-card" aria-label="Corvell Insulation business card">
    <div class="card-top">
      <div class="brand">
        <span class="brand-square"></span>
        <span class="brand-name">Corvell Insulation</span>
      </div>
    </div>

    <div class="card-green"></div>
    <svg class="divider-band" viewBox="0 0 1000 24" aria-hidden="true">
      <path d="M0 0 H1000 V10 H92 L76 24 L60 10 H0 Z" fill="var(--band-dark)"/>
    </svg>

    <div class="person">
      <p class="person-name">Bo Kerrigan</p>
      <p class="person-role">Salesman</p>
    </div>

    <ul class="contact-list">
      <li class="contact-item">
        <svg class="contact-icon" viewBox="0 0 22 22" aria-hidden="true"><circle cx="11" cy="11" r="11" fill="var(--band-dark)"/><path d="M5 11 L11 5.5 L17 11 H15 V16 H7 V11 Z" fill="#fff"/></svg>
        14 Pellmore Ct.
      </li>
      <li class="contact-item no-icon">Brentfield, CA 95418</li>
      <li class="contact-item">
        <svg class="contact-icon" viewBox="0 0 22 22" aria-hidden="true"><circle cx="11" cy="11" r="11" fill="var(--band-dark)"/><path d="M7 5.5 L9.5 5 L10.5 8 L9 9.2 Q10.3 12 12.8 13 L14 11.5 L17 12.5 L16.5 15 Q11 16 7 10 Z" fill="#fff"/></svg>
        (530) 555-0142
      </li>
      <li class="contact-item">
        <svg class="contact-icon" viewBox="0 0 22 22" aria-hidden="true"><circle cx="11" cy="11" r="11" fill="var(--band-dark)"/><rect x="8" y="4.5" width="6" height="13" rx="1.2" fill="#fff"/><rect x="9" y="6" width="4" height="8" fill="var(--band-dark)"/></svg>
        (530) 555-0187
      </li>
      <li class="contact-item">
        <svg class="contact-icon" viewBox="0 0 22 22" aria-hidden="true"><circle cx="11" cy="11" r="11" fill="var(--band-dark)"/><rect x="8" y="5" width="6" height="4" fill="#fff"/><rect x="5.5" y="9" width="11" height="5" rx="1" fill="#fff"/><rect x="8" y="14" width="6" height="3" fill="#fff"/></svg>
        (530) 555-0163
      </li>
      <li class="contact-item">
        <svg class="contact-icon" viewBox="0 0 22 22" aria-hidden="true"><circle cx="11" cy="11" r="11" fill="var(--band-dark)"/><rect x="5" y="7" width="12" height="8.5" rx="1" fill="#fff"/><path d="M5.5 7.5 L11 12 L16.5 7.5" stroke="var(--band-dark)" stroke-width="1.3" fill="none"/></svg>
        bo.kerrigan@corvellinsulation.com
      </li>
      <li class="contact-item">
        <svg class="contact-icon" viewBox="0 0 22 22" aria-hidden="true"><circle cx="11" cy="11" r="11" fill="var(--band-dark)"/><circle cx="11" cy="11" r="6" stroke="#fff" stroke-width="1.3" fill="none"/><ellipse cx="11" cy="11" rx="2.6" ry="6" stroke="#fff" stroke-width="1.1" fill="none"/><path d="M5 11 H17" stroke="#fff" stroke-width="1.1"/></svg>
        www.corvellinsulation.com
      </li>
    </ul>
  </section>
</main>
</body>
</html>
```